Tour operator needs simple coded WordPress site (updated extra payment for coding and guaranteed)

[update 9/7/2015]
If you design a new logo and it gets accepted, even if we use another template with your logo you will get $50
[update 8/7/2015]
Update on questions about dual-language
For dual languages we are happy to set up a second site with the same designs in a second language.
For the design aspect just allow the user to switch between languages with an icon.
For the coding, a replica of the site on a second server will do (to save messing around with multiple language plugins) - we will populate it with Chinese text
[original post]
Simple coded WordPress site for tours
You can choose to design only or design and code ($340 design, $150 bonus for coding)
Open design brief - use your creativity
Will be in 2 languages (English and Chinese) but design needs only to be in one language
Winning design will be chosen only from home page, but the winner must make a second standard template page when chosen at no extra cost.
Must be responsive design
We only need homepage and standard template page design and coding, we will populate the pages
You can use design ideas from our pamphlet if you like - attached
Only a sample logo and colors on website and pamphlet - feel free to change as the current ones seem restrictive
Current website framework only to give an idea of the number of pages and basic menu structure (no need to use existing navigation style or any style at all for that matter, open brief)
http://brightwaterlearningtrips.com.au/
Target Market(s)
Chinese parents of kids 10-14 (the kids will take the tour)
Industry/Entity Type
Tour
Number of Pages Required
2 page
Look and feel
Each slider illustrates characteristics of the customer's brand and the style your logo design should communicate.

```html
<!DOCTYPE html>
<html lang="en">
<head>
<meta charset="utf-8">
<title>Brightwater Learning Trips</title>
<link href="https://fonts.googleapis.com/css2?family=Open+Sans:wght@400;600;700;800&family=Kalam:wght@400&display=swap" rel="stylesheet">
<style>
:root{
  --orange:#f2a31b;
  --orange-dark:#d98a0c;
  --navy:#1f2a44;
  --sky:#2f6fc4;
  --ink:#333;
  --muted:#888;
  --paper:#fff;
  --panel:#f1f1f1;
  --footer:#1e1e1e;
  --red:#d8322b;
}
*{box-sizing:border-box;margin:0;padding:0}
html,body{width:1200px;height:2384px;overflow:hidden}
body{font-family:"Open Sans",Arial,sans-serif;color:var(--ink);background:var(--sky);position:relative}
.site-header{position:absolute;left:0;top:0;width:1200px;height:104px;background:var(--paper);border-bottom:4px solid var(--orange)}
.brand{position:absolute;left:92px;top:22px;display:flex;align-items:center;gap:12px}
.brand-dot{width:46px;height:46px;border-radius:50%;background:var(--orange)}
.brand-name{font-weight:800;font-size:22px;color:var(--navy);line-height:1.05}
.main-nav{position:absolute;left:476px;top:40px;display:flex;gap:8px}
.main-nav a{font-size:13px;font-weight:600;color:#555;text-decoration:none;padding:8px 22px;text-transform:uppercase}
.main-nav a.active{background:var(--orange);color:#fff}
.header-tools{position:absolute;right:90px;top:16px;display:flex;align-items:center;gap:10px;font-size:14px}
.header-tools .call{color:var(--red);font-weight:700}
.lang{border:1px solid #ccc;font-size:11px;padding:2px 6px;color:#555}
.social{position:absolute;right:90px;top:50px;display:flex;gap:6px}
.social span{width:22px;height:22px;border-radius:50%;background:#3a8fd8}
.social span:nth-child(2){background:#2a5fa8}
.social span:nth-child(3){background:#d34836}
.social span:nth-child(4){background:#2aa0d8}

.backdrop{position:absolute;left:0;top:108px;width:1200px;height:1912px;background:linear-gradient(180deg,#1f5fb7 0%,#3c86d8 25%,#4a8fd6 50%,#2f6fc4 100%)}
.hero{position:absolute;left:110px;top:150px;width:1000px;height:448px;border:6px solid #fff;background:linear-gradient(180deg,#8ec9ef 0%,#cfe9f7 40%,#3fc2c9 55%,#e9dcc0 80%,#f3e6cc 100%);box-shadow:0 6px 16px rgba(0,0,0,.3)}
.hero-tag{position:absolute;left:24px;top:176px}
.hero-tag .line1{display:inline-block;background:var(--orange);color:var(--navy);font-weight:800;font-size:28px;padding:8px 18px;text-transform:uppercase}
.hero-tag .line2{display:block;width:fit-content;margin-top:6px;background:var(--navy);color:#fff;font-weight:600;font-size:22px;padding:8px 18px}

.features{position:absolute;left:110px;top:628px;width:1000px;height:432px;background:var(--orange);display:flex;gap:40px;padding:28px 36px}
.feature{flex:1}
.feature h2{font-size:20px;font-weight:800;color:var(--navy);text-transform:uppercase;margin-bottom:10px}
.feature .photo{height:150px;border:4px solid #fff}
.feature p{font-size:12px;color:#fff;line-height:1.45;margin:14px 0}
.btn{display:inline-block;background:#fff;color:var(--ink);font-size:11px;font-weight:700;padding:5px 12px}
.btn.dark{background:var(--orange-dark);color:#fff}

.content{position:absolute;left:110px;top:1090px;width:1000px;height:930px;background:var(--paper);padding:24px 24px}
.section-title{font-size:22px;font-weight:700;color:#222;border-bottom:1px solid #ddd;padding-bottom:8px}
.offers{position:relative;height:330px}
.offers .label{position:absolute;top:58px;font-size:13px;color:#555}
.sponsored-photo{position:absolute;left:0;top:96px;width:170px;height:150px;background:linear-gradient(180deg,#8fc2e8,#6b9a5a 70%,#b7a88a)}
.offer-card{position:absolute;top:96px;width:190px;height:186px;background:var(--panel);border:1px solid #e2e2e2;padding:12px;text-align:center}
.offer-card .photo{height:60px;width:90px;margin:0 auto 10px}
.offer-card h3{font-size:12px;color:var(--red);font-weight:700}
.offer-card p{font-size:10px;color:var(--muted);margin:6px 0 8px;line-height:1.35}
.events{display:flex;gap:44px;margin-top:22px;padding:0 50px}
.event{flex:1}
.event .photo{height:96px}
.event h4{font-size:12px;font-weight:700;margin-top:8px}
.event p{font-size:10px;color:var(--muted);line-height:1.35;margin-top:4px}
.stays{display:flex;gap:30px;margin-top:22px;padding:0 12px}
.stay{flex:1;display:flex;gap:14px}
.stay .photo{width:220px;height:186px;flex:none}
.stay h4{font-size:13px;font-weight:700;margin-top:6px}
.stay p{font-size:11px;color:var(--muted);line-height:1.45;margin:8px 0 12px}

.site-footer{position:absolute;left:0;top:2020px;width:1200px;height:364px;background:var(--footer);color:#ccc}
.footer-links{position:absolute;left:200px;top:60px;display:grid;grid-template-columns:150px 150px;row-gap:10px;font-size:11px}
.follow{position:absolute;left:600px;top:50px;font-family:"Kalam",cursive;color:#3fb0e0;font-size:22px;transform:rotate(-12deg)}
.footer-social{position:absolute;left:560px;top:110px;display:flex;gap:12px}
.footer-social span{width:30px;height:30px;background:#3a8fd8}
.footer-brand{position:absolute;left:880px;top:80px;display:flex;align-items:center;gap:12px}
.footer-brand .brand-dot{width:40px;height:40px}
.footer-brand .brand-name{color:#fff;font-size:20px}
.footer-divider{position:absolute;left:860px;top:64px;width:1px;height:90px;background:#444}
.copyright{position:absolute;left:0;width:100%;top:232px;text-align:center;font-size:9px;color:#888}
.download-bar{position:absolute;left:220px;top:300px;width:780px;height:42px;background:#2b2b2b;border-top:3px solid var(--orange);display:flex;align-items:center}
.download-bar .free{background:var(--orange);color:var(--navy);font-weight:800;font-size:16px;padding:0 22px;height:100%;display:flex;align-items:center;margin-left:48px}
.download-bar .item{flex:1;text-align:center;font-size:11px;font-weight:700;color:#fff;line-height:1.2}
.download-bar .item small{display:block;font-size:8px;color:#aaa;font-weight:400}
.booklet{position:absolute;left:232px;top:278px;width:40px;height:60px;background:linear-gradient(180deg,#3a7fd0,#7cb2e6)}
</style>
</head>
<body>

<header class="site-header">
  <div class="brand"><span class="brand-dot"></span><span class="brand-name">Brightwater<br>Learning Trips</span></div>
  <nav class="main-nav"><a class="active" href="#">Home</a><a href="#">Tours</a><a href="#">Contact</a></nav>
  <div class="header-tools"><span class="call">Call Us: 1800 555 204</span><span class="lang">English ▾</span></div>
  <div class="social"><span></span><span></span><span></span><span></span></div>
</header>

<div class="backdrop"></div>

<section class="hero" role="img" aria-label="Students walking along a tropical beach with turquoise water">
  <div class="hero-tag"><span class="line1">Educational, Safe</span><span class="line2">Culturally enlightening and fun</span></div>
</section>

<section class="features">
  <article class="feature">
    <h2>Specials &amp; Packages</h2>
    <div class="photo" role="img" aria-label="Ornate temple under blue sky" style="background:linear-gradient(180deg,#5fa5e0,#c98a4a 60%,#8a5a2e)"></div>
    <p>Join our student tours to great places and learn about local culture with our friendly guides through the summer.</p>
    <a class="btn" href="#">More Info</a>
  </article>
  <article class="feature">
    <h2>Kenai Fjords</h2>
    <div class="photo" role="img" aria-label="Group of young travellers gathered outdoors" style="background:linear-gradient(180deg,#9cc6e8,#b0413a 55%,#6a8a4a)"></div>
    <p>Lorem ipsum and discover the glaciers and amazing wildlife of the fjords with our expert guides on every day tour.</p>
    <a class="btn" href="#">More Info</a>
  </article>
  <article class="feature">
    <h2>Prince William Sound</h2>
    <div class="photo" role="img" aria-label="Ocean cruise among glaciers" style="background:linear-gradient(180deg,#7fb7e6,#e0e8ef 50%,#3b6f9c)"></div>
    <p>Lorem ipsum and discover the calm waters and amazing wildlife of the sound with our expert guides on every day tour.</p>
    <a class="btn" href="#">More Info</a>
  </article>
</section>

<main class="content">
  <section class="offers">
    <h2 class="section-title">Offers</h2>
    <span class="label" style="left:0">Sponsored</span>
    <span class="label" style="left:180px">Special Offers</span>
    <div class="sponsored-photo" role="img" aria-label="Historic building among trees"></div>
    <a class="btn dark" href="#" style="position:absolute;left:0;top:262px">More</a>
    <div class="offer-card" style="left:240px">
      <div class="photo" role="img" aria-label="Souvenir shop" style="background:linear-gradient(#6aa6d8,#b98a56)"></div>
      <h3>10% Off All Merchandise</h3>
      <p>Save on bags, shirts and gifts when you book a tour this month.</p>
      <a class="btn dark" href="#">View Offer</a>
    </div>
    <div class="offer-card" style="left:470px">
      <div class="photo" role="img" aria-label="Sandy beach" style="background:linear-gradient(#7cc0e8,#e5d3a8)"></div>
      <h3>25-30% Off - Coral Point Beach</h3>
      <p>Save on beach stays for groups booking before the summer break.</p>
      <a class="btn dark" href="#">View Offer</a>
    </div>
    <div class="offer-card" style="left:700px">
      <div class="photo" role="img" aria-label="Summer resort lawn" style="background:linear-gradient(#8cc6ea,#6e9a4e)"></div>
      <h3>10% Off Maple Ridge Summer</h3>
      <p>Save on summer camp places when you book with a friend.</p>
      <a class="btn dark" href="#">View Offer</a>
    </div>
  </section>

  <section>
    <h2 class="section-title">Featured Events</h2>
    <div class="events">
      <article class="event">
        <div class="photo" role="img" aria-label="Coastal bay with boats" style="background:linear-gradient(#7bbbe6,#2f9fb0 55%,#c9b98e)"></div>
        <h4>LOREM IPSUM DOLOR SIT AMET</h4>
        <p>Short event details and dates for the coming season.</p>
      </article>
      <article class="event">
        <div class="photo" role="img" aria-label="Historic town buildings" style="background:linear-gradient(#9cc7e8,#b08a66 55%,#6a5a48)"></div>
        <h4>LOREM IPSUM DOLOR SIT AMET</h4>
        <p>Short event details and dates for the coming season.</p>
      </article>
      <article class="event">
        <div class="photo" role="img" aria-label="Harbour city skyline" style="background:linear-gradient(#6aa8dc,#d7c9a8 55%,#2f6f9c)"></div>
        <h4>LOREM IPSUM DOLOR SIT AMET</h4>
        <p>Short event details and dates for the coming season.</p>
      </article>
    </div>
  </section>

  <section style="margin-top:30px">
    <h2 class="section-title">Places to Stay</h2>
    <div class="stays">
      <article class="stay">
        <div class="photo" role="img" aria-label="Riverside lodge building" style="background:linear-gradient(#b9d6ee,#8a7a66 55%,#5c6a4a)"></div>
        <div><h4>LOREM IPSUM DOLOR SIT</h4><p>Comfortable rooms for student groups with meals, study areas and friendly staff on site every day.</p><a class="btn dark" href="#">Read More</a></div>
      </article>
      <article class="stay">
        <div class="photo" role="img" aria-label="Waterfall in green forest" style="background:linear-gradient(#a9cbe6,#d8e4ea 40%,#4f7a4a)"></div>
        <div><h4>LOREM IPSUM DOLOR SIT</h4><p>Quiet cabins near nature trails, with guided walks and safe spaces for young travellers.</p><a class="btn dark" href="#">Read More</a></div>
      </article>
    </div>
  </section>
</main>

<footer class="site-footer">
  <div class="footer-links">
    <span>HOME</span><span>PLACES TO GO</span>
    <span>DESTINATIONS</span><span>CONTACT</span>
    <span>THINGS TO DO</span><span>TRAVEL GUIDE</span>
    <span>PLACES TO STAY</span>
  </div>
  <div class="follow">Follow Us</div>
  <div class="footer-social"><span></span><span></span><span></span></div>
  <div class="footer-divider"></div>
  <div class="footer-brand"><span class="brand-dot"></span><span class="brand-name">Brightwater<br>Learning Trips</span></div>
  <div class="copyright">COPYRIGHT 2015 BRIGHTWATER LEARNING TRIPS. ALL RIGHTS RESERVED.</div>
  <div class="download-bar">
    <span class="free">FREE DOWNLOAD</span>
    <span class="item">VACATION GUIDE<small>Plan your trip</small></span>
    <span class="item">INTO THE MAP<small>Find places</small></span>
    <span class="item">NEWSLETTER<small>Stay updated</small></span>
  </div>
  <div class="booklet" role="img" aria-label="Travel guide booklet cover"></div>
</footer>

</body>
</html>
```